Marrowgate Pictures Pty needs poster design for Australian feature film thriller

In the tradition of great classic “serial killer” films such as Velvet Tenant and Harbinger, the thriller "Quiet Stranger" promises mystery, excitement and, of course, the ultimate battle between good and evil. A modern city is hit with a string of continuing inexplicable murders of seemingly random women from different cultural and socio-economic backgrounds. The audience journeys with the murderer as he carries out his deadly deeds. We also follow the dedicated police force which will not let go of every possible lead. What happens when the murderer meets the last standing policewoman on his trail will leave audiences in shock!

We are looking for a poster design for this film which is a tribute to Howard Keswick's film "Shadow at Nine." Poster should be classy and grabs the viewer emotionally.

The film "Quiet Stranger" is in post-production. The film will be sent to international film festivals. I've uploaded the following:
1. some posters I like (please be creative in your own style)
2. a credit list that needs to be on the poster
3. photos of "The quiet Stranger" facing different directions and in different emotions
4. some of his female victims for your reference and inspiration
5. some on-set photos of Quiet Stranger with some of his potential victims for your reference and inspiration

Target Market(s)

International Western audiences who love thrillers

Requirements
Must have
• Something that grabs the emotions and intrigues the viewer to come see the film
Nice to have
• n/a
Should not have
• n/a

```html
<!DOCTYPE html>
<html lang="en">
<head>
<meta charset="utf-8">
<title>Quiet Stranger — Poster</title>
<link rel="stylesheet" href="https://fonts.googleapis.com/css2?family=Oswald:wght@300;400;500&display=swap">
<style>
  :root {
    --paper: #dcb99b;
    --paper-light: #e8cdb4;
    --paper-dark: #c49a7c;
    --orange: #e0782a;
    --orange-deep: #c04f1c;
    --ink: #050403;
    --cream: #f2dfcc;
    --title: #dcb49a;
    --credit: #efe3d6;
  }
  * { margin: 0; padding: 0; box-sizing: border-box; }
  html, body { width: 872px; height: 1200px; overflow: hidden; background: var(--paper); }
  .poster {
    position: relative;
    width: 872px;
    height: 1200px;
    overflow: hidden;
    font-family: "Oswald", "Arial Narrow", sans-serif;
    background:
      radial-gradient(ellipse at 15% 20%, rgba(255,240,225,.35), transparent 55%),
      radial-gradient(ellipse at 90% 10%, rgba(150,100,70,.25), transparent 45%),
      radial-gradient(ellipse at 5% 80%, rgba(160,110,80,.3), transparent 50%),
      linear-gradient(180deg, var(--paper-light), var(--paper) 50%, var(--paper-dark));
  }
  .backdrop {
    position: absolute;
    left: 82px; top: 123px;
    width: 722px; height: 720px;
    background:
      radial-gradient(ellipse at 20% 40%, rgba(255,170,80,.35), transparent 60%),
      linear-gradient(90deg, var(--orange) 0%, #d8692a 60%, var(--orange-deep) 100%);
  }
  .portrait {
    position: absolute;
    left: 0; top: 0;
    width: 872px; height: 1200px;
  }
  .cast {
    position: absolute;
    top: 36px; left: 83px; right: 70px;
    display: flex;
    justify-content: space-between;
    color: var(--cream);
    font-weight: 300;
    text-transform: uppercase;
    text-shadow: 0 1px 2px rgba(60,30,10,.45);
  }
  .cast-name { display: flex; flex-direction: column; line-height: .95; }
  .cast-first { font-size: 22px; letter-spacing: -.5px; }
  .cast-last { font-size: 34px; letter-spacing: -.8px; }
  .title {
    position: absolute;
    right: 64px; top: 780px;
    text-align: right;
    color: var(--title);
    font-weight: 500;
    font-size: 128px;
    line-height: .86;
    letter-spacing: -1px;
    text-transform: uppercase;
  }
  .credits {
    position: absolute;
    right: 64px; top: 1030px;
    color: var(--credit);
    font-weight: 400;
    font-size: 16px;
    letter-spacing: -.4px;
    text-transform: uppercase;
    text-align: right;
  }
  .credit-line {
    display: flex;
    justify-content: flex-end;
    align-items: center;
    gap: 4px;
    white-space: nowrap;
    height: 26px;
  }
  .credit-line .gap { width: 14px; }
  .label {
    display: inline-flex;
    flex-direction: column;
    font-size: 6px;
    line-height: 1;
    text-align: right;
    letter-spacing: 0;
  }
  .copyright { font-size: 12px; height: 20px; }
</style>
</head>
<body>
<main class="poster">
  <div class="backdrop"></div>

  <svg class="portrait" viewBox="0 0 872 1200" role="img" aria-label="Photograph of the lead actor in deep shadow, head and shoulders, dark jacket over a blue shirt">
    <defs>
      <linearGradient id="shadow" x1="0" y1="0" x2="0" y2="1">
        <stop offset="0" stop-color="#0a0705"/>
        <stop offset=".45" stop-color="#1c120c"/>
        <stop offset=".75" stop-color="#070505"/>
        <stop offset="1" stop-color="#040404"/>
      </linearGradient>
    </defs>
    <path fill="url(#shadow)" d="M0 835 L175 800 C210 760 220 700 230 620 C205 520 185 330 200 220 C220 120 300 65 420 58 C560 55 650 110 690 220 C710 320 690 560 660 660 C700 740 790 760 872 790 L872 1200 L0 1200 Z"/>
  </svg>

  <header class="cast">
    <div class="cast-name"><span class="cast-first">Dev</span><span class="cast-last">Malhotra</span></div>
    <div class="cast-name"><span class="cast-first">Nina</span><span class="cast-last">Holloway</span></div>
    <div class="cast-name"><span class="cast-first">Mateo</span><span class="cast-last">Rivas</span></div>
    <div class="cast-name"><span class="cast-first">Greg</span><span class="cast-last">Thornley</span></div>
    <div class="cast-name"><span class="cast-first">Callum</span><span class="cast-last">Price</span></div>
  </header>

  <h1 class="title">Quiet<br>Stranger</h1>

  <section class="credits">
    <p class="credit-line">Ferncliff Films Pty Ltd &amp; Marrowgate Pictures Pty Ltd <span class="label"><span>presents a</span></span> Rowan Ellison Film “Quiet Stranger”</p>
    <p class="credit-line"><span class="label"><span>starring</span></span> Dev Malhotra, Nina Holloway, Mateo Rivas, Greg Thornley, Callum Price</p>
    <p class="credit-line"><span class="label"><span>executive</span><span>producers</span></span> Dev Malhotra &amp; Rowan Ellison<span class="gap"></span><span class="label"><span>director of</span><span>photography</span></span>&amp;<span class="label"><span>film</span><span>editor</span></span> Owen Parfitt<span class="gap"></span><span class="label"><span>sound</span><span>design</span></span> Liam Cordell<span class="gap"></span><span class="label"><span>music</span><span>composer</span></span> Reid Haskett</p>
    <p class="credit-line"><span class="label"><span>casting</span></span> Marrowgate Pictures Pty Ltd<span class="gap"></span><span class="label"><span>art</span><span>direction</span></span> Janelle Morcombe &amp; Peter Voss<span class="gap"></span><span class="label"><span>makeup</span><span>design</span></span> Kate Darrow</p>
    <p class="credit-line"><span class="label"><span>costume</span><span>design</span></span> Elsa Winthrop<span class="gap"></span><span class="label"><span>original</span><span>story</span></span> Dev Malhotra<span class="gap"></span><span class="label"><span>screenplay</span></span> Nadia Farres &amp; Rowan Ellison<span class="gap"></span><span class="label"><span>directed</span><span>by</span></span> Rowan Ellison</p>
    <p class="credit-line copyright">Copyright © 2016 Ferncliff Films Pty Ltd &amp; Marrowgate Pictures Pty Ltd. All Rights Reserved.</p>
  </section>
</main>
</body>
</html>
```